logo and label design for a vegan skincare Called Plantavive

We need a logo and label design for a skincare brand called plantavive based in Australia. The products are 100% natural, Australian made, small batch, vegan, cruelty-free, ethical and sustainable beauty products. The secret of our skin care products are their naturally active ingredients.
They are potent, yet incredibly gentle on sensitive skin. We believe in investing in only the highest quality and ethical ingredients to ensure we are creating products we can stand behind.
Our products use: Naturally delivered ingredients; Organic ingredients where is possible; Australian oils, fruits & Extracts; Aromatherapy oils; sustainable & ethical ingredients; natural preservatives.
Our products don't use: sulphates; parabens; phthalates; Petrochemicals; synthetic colours; synthetic fragrances. All label must be design for an amber bottle.
Label Requirements:
* 300 DPI minimum
* All fonts have been outlined
* 3mm Bleed included in artwork
Colors
Designer to choose colors to be used in the design.
Look and feel
Each slider illustrates characteristics of the customer's brand and the style your logo design should communicate.

```html
<!DOCTYPE html>
<html lang="en">
<head>
<meta charset="utf-8">
<title>Plantavive skincare labels</title>
<link href="https://fonts.googleapis.com/css2?family=Oswald:wght@500;600&family=Montserrat:wght@500&family=Kaushan+Script&display=swap" rel="stylesheet">
<style>
  :root {
    --page: #e9e9e9;
    --label: #e7dfd2;
    --ink: #1b1b1b;
    --rule: #111111;
  }
  * { box-sizing: border-box; margin: 0; padding: 0; }
  html, body { width: 1200px; height: 663px; overflow: hidden; }
  body {
    background: linear-gradient(#f1f1f1, #dedede);
    position: relative;
    color: var(--ink);
  }
  .label {
    position: absolute;
    width: 21.4em;
    height: 27.2em;
    background: var(--label);
    display: flex;
    flex-direction: column;
    align-items: center;
    text-align: center;
    padding: 1em 1.4em 2.2em;
    box-shadow: 0 0.3em 1em rgba(0,0,0,0.12);
  }
  .label::before, .label::after {
    content: "";
    position: absolute;
    left: 0; right: 0;
    border-top: 0.45em solid var(--rule);
    border-bottom: 0.12em solid var(--rule);
    height: 0.85em;
  }
  .label::before { top: 0.35em; }
  .label::after { bottom: 0.5em; }

  .brand-square {
    position: relative;
    z-index: 1;
    width: 3.7em;
    height: 3.7em;
    background: var(--rule);
    flex: none;
  }
  .brand-name {
    font-family: "Montserrat", sans-serif;
    font-weight: 500;
    font-size: 1.55em;
    letter-spacing: 0.06em;
    margin-top: 0.35em;
  }
  .product-name {
    font-family: "Oswald", sans-serif;
    font-weight: 600;
    font-size: 2.25em;
    line-height: 1.15;
    letter-spacing: 0.01em;
    margin-top: auto;
    text-transform: uppercase;
  }
  .ingredients {
    font-family: "Kaushan Script", cursive;
    font-size: 1.15em;
    width: 100%;
    border-top: 0.09em solid var(--rule);
    border-bottom: 0.09em solid var(--rule);
    padding: 0.45em 0;
    margin-top: 0.4em;
    width: 92%;
  }
  .skin-types {
    font-family: "Oswald", sans-serif;
    font-weight: 500;
    font-size: 1.25em;
    margin-top: 0.6em;
  }
  .badges {
    display: flex;
    gap: 0.7em;
    align-items: center;
    margin-top: 0.6em;
  }
  .badge {
    width: 2.5em;
    height: 2.5em;
    border: 0.18em solid var(--rule);
    border-radius: 50%;
  }
  .badge.triangle {
    border: none;
    border-radius: 0;
    width: 2.6em;
    background: var(--rule);
    clip-path: polygon(50% 0, 100% 100%, 0 100%);
  }
  .dots { font-family: "Montserrat", sans-serif; font-size: 1em; line-height: 0.8; margin-top: 0.2em; letter-spacing: 0.1em; }
  .volume { font-family: "Montserrat", sans-serif; font-size: 1.1em; }

  .cleanser { font-size: 10px; left: 91px; top: 275px; }
  .mist { font-size: 7.7px; left: 382px; top: 338px; height: 28.6em; width: 21.4em; }
  .mask { font-size: 9px; left: 610px; top: 340px; width: 31.5em; height: 27.2em; }
  .mask .product-name { font-size: 2.4em; }
  .eye { font-size: 7.1px; left: 971px; top: 356px; height: 30.5em; }
</style>
</head>
<body>
  <section class="label cleanser">
    <div class="brand-square"></div>
    <p class="brand-name">PLANTAVIVE</p>
    <h2 class="product-name">Purifying<br>Gel Cleanser</h2>
    <p class="ingredients">· Lemon Tea Tree &amp; Vitamin E ·</p>
    <p class="skin-types">- ALL SKIN TYPES -</p>
    <div class="badges"><span class="badge"></span><span class="badge"></span><span class="badge"></span><span class="badge triangle"></span></div>
    <p class="dots">•••</p>
    <p class="volume">200 ml</p>
  </section>

  <section class="label mist">
    <div class="brand-square"></div>
    <p class="brand-name">PLANTAVIVE</p>
    <h2 class="product-name">Natural<br>AHA Toning Mist</h2>
    <p class="ingredients">· Quandong · Papaya · Lemongrass ·</p>
    <p class="skin-types">- ALL SKIN TYPES -</p>
    <div class="badges"><span class="badge"></span><span class="badge"></span><span class="badge"></span><span class="badge triangle"></span></div>
    <p class="dots">•••</p>
    <p class="volume">100 ml</p>
  </section>

  <section class="label mask">
    <div class="brand-square"></div>
    <p class="brand-name">PLANTAVIVE</p>
    <h2 class="product-name">Pink Clay Calming Mask</h2>
    <p class="ingredients">· Calendula · Chamomile · Aloe Vera ·</p>
    <p class="skin-types">- ALL SKIN TYPES -</p>
    <div class="badges"><span class="badge"></span><span class="badge"></span><span class="badge"></span><span class="badge triangle"></span></div>
    <p class="dots">•••</p>
    <p class="volume">90 gr</p>
  </section>

  <section class="label eye">
    <div class="brand-square"></div>
    <p class="brand-name">PLANTAVIVE</p>
    <h2 class="product-name">Intensive<br>Eye Cream</h2>
    <p class="ingredients">· Resveratrol · Shea Butter · Cucumber ·</p>
    <p class="skin-types">- ALL SKIN TYPES -</p>
    <div class="badges"><span class="badge"></span><span class="badge"></span><span class="badge"></span><span class="badge triangle"></span></div>
    <p class="dots">•••</p>
    <p class="volume">30 ml</p>
  </section>
</body>
</html>
```